Lantern Hearthworks Business Cards

Looking to create simple business cards that highlight our unique three sided triangle fire pit design with the colors and font of our logo, listed below.

Requirements
Must have
• Looking for something simple that includes a picture of our fire pit with name, website (lanternhearthworks.com), phone number and email. Want to keep the color mostly orange and black.
• Font is gotham(medium) and orange color code is #ee6e22

```html
<!DOCTYPE html>
<html lang="en">
<head>
<meta charset="utf-8">
<title>Lantern Hearthworks Business Cards</title>
<link href="https://fonts.googleapis.com/css2?family=Montserrat:wght@400;500;600&display=swap" rel="stylesheet">
<style>
  :root {
    --backdrop: #cfc6b8;
    --card-black: #0b0b0b;
    --ember: #ee6e22;
    --flame: #f39a3c;
    --coral: #e8473d;
    --white: #ffffff;
    --soft-white: #e6e6e6;
    --rule: #8a8a8a;
    --gravel-light: #4b4b4b;
    --gravel-mid: #343434;
    --gravel-dark: #1a1a1a;
    --steel: #141414;
  }
  html, body {
    margin: 0;
    padding: 0;
    overflow: hidden;
  }
  body {
    width: 900px;
    height: 1200px;
    position: relative;
    background: var(--backdrop);
    font-family: "Montserrat", Arial, sans-serif;
  }
  .card {
    position: absolute;
    left: 82px;
    width: 734px;
    height: 428px;
    border-radius: 20px;
    overflow: hidden;
    box-shadow: 0 6px 18px rgba(0,0,0,0.35);
  }
  .card-front {
    top: 138px;
    background: var(--card-black);
  }
  .card-back {
    top: 634px;
  }
  .brand-dot {
    position: absolute;
    left: 72px;
    top: 62px;
    width: 80px;
    height: 80px;
    border-radius: 50%;
    background: var(--ember);
  }
  .brand-rule {
    position: absolute;
    left: 184px;
    top: 49px;
    width: 1px;
    height: 126px;
    background: var(--rule);
  }
  .brand-name {
    position: absolute;
    left: 198px;
    top: 78px;
    margin: 0;
    font-weight: 500;
    font-size: 29px;
    line-height: 31px;
    letter-spacing: 3px;
    color: var(--ember);
    text-transform: uppercase;
  }
  .holder {
    position: absolute;
    right: 330px;
    top: 320px;
    text-align: right;
  }
  .holder-name {
    margin: 0;
    font-weight: 600;
    font-size: 22px;
    letter-spacing: 1px;
    color: var(--white);
  }
  .holder-title {
    margin: 7px 0 0;
    font-weight: 600;
    font-size: 15.5px;
    letter-spacing: 0.3px;
    color: var(--coral);
  }
  .contact-rule {
    position: absolute;
    left: 419px;
    top: 307px;
    width: 1px;
    height: 76px;
    background: var(--rule);
  }
  .contact-list {
    position: absolute;
    left: 438px;
    top: 301px;
    margin: 0;
    padding: 0;
    list-style: none;
  }
  .contact-item {
    display: flex;
    align-items: center;
    height: 29px;
    font-size: 16px;
    color: var(--soft-white);
  }
  .contact-icon {
    width: 16px;
    height: 16px;
    margin-right: 12px;
    fill: var(--coral);
  }
  .product-photo {
    position: absolute;
    inset: 0;
    background:
      radial-gradient(ellipse 110px 80px at 58% 36%, var(--flame), rgba(238,110,34,0.9) 35%, rgba(238,110,34,0) 100%),
      radial-gradient(ellipse 70px 60px at 46% 50%, rgba(238,110,34,0.7), rgba(238,110,34,0) 100%),
      radial-gradient(ellipse 190px 200px at 50% 42%, var(--steel), rgba(20,20,20,0.85) 55%, rgba(20,20,20,0) 100%),
      linear-gradient(160deg, var(--gravel-light), var(--gravel-mid) 55%, var(--gravel-dark));
  }
  .back-url {
    position: absolute;
    left: 0;
    right: 0;
    bottom: 20px;
    margin: 0;
    text-align: center;
    font-weight: 600;
    font-size: 17px;
    letter-spacing: 0.5px;
    color: var(--white);
  }
  .back-url .accent {
    color: var(--ember);
  }
</style>
</head>
<body>
  <section class="card card-front">
    <div class="brand-dot" aria-hidden="true"></div>
    <div class="brand-rule"></div>
    <h1 class="brand-name">Lantern<br>Hearthworks</h1>

    <div class="holder">
      <p class="holder-name">EVAN MERCER</p>
      <p class="holder-title">MANAGING DIRECTOR</p>
    </div>

    <div class="contact-rule"></div>

    <ul class="contact-list">
      <li class="contact-item">
        <svg class="contact-icon" viewBox="0 0 16 16" aria-hidden="true">
          <path d="M3.6 1.2l2.2 2.6c.3.4.3.9 0 1.2L4.6 6.3c.9 2 2.6 3.8 4.7 4.8l1.3-1.2c.4-.3.9-.3 1.2 0l2.6 2.2c.4.3.4.9 0 1.3l-1.3 1.3c-.6.6-1.5.8-2.3.5C6 13.6 2.4 10 .8 5.1.5 4.3.7 3.4 1.3 2.8L2.3 1.2c.4-.4 1-.4 1.3 0z"/>
        </svg>
        555-310-4827
      </li>
      <li class="contact-item">
        <svg class="contact-icon" viewBox="0 0 16 16" aria-hidden="true">
          <path d="M1 3h14v1L8 9 1 4z"/>
          <path d="M1 5.5l7 5 7-5V13H1z"/>
        </svg>
        evan@hearthmail.com
      </li>
      <li class="contact-item">
        <svg class="contact-icon" viewBox="0 0 16 16" aria-hidden="true">
          <g fill="none" stroke="#e8473d" stroke-width="1.3">
            <circle cx="8" cy="8" r="6.5"/>
            <ellipse cx="8" cy="8" rx="3" ry="6.5"/>
            <line x1="1.5" y1="8" x2="14.5" y2="8"/>
            <path d="M2.6 4.6h10.8M2.6 11.4h10.8"/>
          </g>
        </svg>
        www.lanternhearthworks.com
      </li>
    </ul>
  </section>

  <section class="card card-back">
    <div class="product-photo" role="img" aria-label="Photo from above of a three-sided triangular steel fire pit burning wood with orange flames, set on dark gravel"></div>
    <p class="back-url">WWW.LANTERN<span class="accent">HEARTHWORKS</span>.COM</p>
  </section>
</body>
</html>
```